New & Improved QUILLAN Business Card

I would like a two sided business card one side dedicated to home automation (security camera installation, television & sound bar mounting (hidden wires optional) , sink installation, fireplace mounting, chandelier installation and one side dedicated to all electronic repairs, In ex: pelmar band repairs, computer, Vorta, laptop repairs, Zenphone's, Kelvora and etc.. Using the colors on this flyer. The phone number &email I want on both sides is (555) 314-2790 & Help@Quillan-example.support. SAME COLOR AS THE FLYER ATTACHED.

Target Market(s)

EVERYONE.

Contact Information for Business Card

I would like a two sided business card one side dedicated to home automation (security camera installation, television & sound bar mounting (hidden wires optional) , sink installation, fireplace mounting, chandelier installation and one side dedicated to all electronic repairs, In ex: pelmar band repairs, computer, Vorta, laptop repairs, Zenphone's, Kelvora and etc.. Using the colors on this flyer. The phone number &email I want on both sides is (555) 314-2790 & Help@Quillan-example.support

Requirements
Must have
• -TV MOUNTING
-HOME AUTOMATION
-SECURITY CAMERA INSTALLATION
-ALL ELECTRONIC REPAIRS
- (555) 314-2790
-Help@Quillan-example.support
-SAME COLOR AS THE FLYER
Nice to have
• Same colors & concept as the flyer attached below.
Should not have
• DO NOT DO A DIFF COLOR I WANT SAME COLOR AS THE FLYER ATTACHED.

```html
<!DOCTYPE html>
<html lang="en">
<head>
<meta charset="utf-8">
<title>QUILLAN Business Card</title>
<link rel="stylesheet" href="https://fonts.googleapis.com/css2?family=Open+Sans:wght@400;600;700;800&display=swap">
<style>
  :root {
    --pink: #e8439a;
    --pink-deep: #d2307f;
    --pink-light: #f272b5;
    --ink: #1c1c1e;
    --charcoal: #26262a;
    --white: #ffffff;
    --grey: #e6e6e8;
    --grey-mid: #bdbdc2;
    --stage: #3a3a3d;
  }
  * { box-sizing: border-box; margin: 0; padding: 0; }
  html, body { width: 1200px; height: 780px; overflow: hidden; }
  body {
    background: var(--stage);
    font-family: "Open Sans", Arial, sans-serif;
    position: relative;
  }
  .card {
    position: absolute;
    top: 60px;
    width: 380px;
    height: 660px;
    overflow: hidden;
    border-radius: 4px;
    box-shadow: 0 10px 30px rgba(0,0,0,.35);
  }
  .card > * { position: absolute; }
  .card-shape { inset: 0; width: 100%; height: 100%; }

  /* Repairs side */
  .card--repairs { left: 170px; background: var(--white); }
  .wordmark {
    left: 0; right: 0; text-align: center;
    font-weight: 600; letter-spacing: .42em; text-indent: .42em;
  }
  .card--repairs .wordmark { top: 96px; font-size: 30px; color: var(--white); }
  .device-labels {
    top: 150px; left: 30px; right: 30px;
    display: flex; justify-content: space-between;
  }
  .device-label {
    width: 92px; text-align: center;
    font-size: 9px; font-weight: 600; letter-spacing: .12em;
    color: rgba(255,255,255,.45);
  }
  .device-illustration {
    top: 222px; left: 60px; width: 260px; height: 220px;
    border-radius: 6px;
    background: linear-gradient(160deg, #f2f2f4 0%, #c9c9cf 55%, #6a6a70 100%);
  }
  .tagline {
    top: 468px; left: 0; right: 0; text-align: center;
    font-size: 17px; font-weight: 700; line-height: 1.2;
    color: var(--ink); text-transform: uppercase;
  }
  .service-title {
    top: 522px; left: 0; right: 0; text-align: center;
    font-size: 21px; font-weight: 800; color: var(--pink);
  }
  .phone-pill {
    top: 560px; left: 24px; right: 24px; height: 34px;
    border-radius: 17px; background: var(--ink);
    display: flex; align-items: center; justify-content: center; gap: 8px;
    font-size: 19px; font-weight: 600; color: var(--pink);
  }
  .email-line {
    top: 606px; left: 34px;
    display: flex; align-items: center; gap: 8px;
    font-size: 15px; color: var(--ink);
  }

  /* Home automation side */
  .card--automation { left: 650px; background: var(--charcoal); }
  .card--automation .wordmark { top: 44px; font-size: 30px; color: var(--pink); }
  .side-title {
    top: 92px; left: 0; right: 0; text-align: center;
    font-size: 16px; font-weight: 800; color: var(--white); letter-spacing: .02em;
  }
  .service-list {
    top: 134px; left: 34px; right: 20px; list-style: none;
    display: flex; flex-direction: column; gap: 12px;
  }
  .service-item {
    display: flex; align-items: flex-start; gap: 10px;
    font-size: 15px; color: var(--white); line-height: 1.25;
  }
  .service-item svg { flex: none; margin-top: 2px; }
  .photo-row {
    top: 362px; left: 18px; right: 18px;
    display: flex; gap: 8px;
  }
  .photo-tile {
    flex: 1; height: 84px; border-radius: 4px; overflow: hidden;
    background: var(--white); position: relative;
  }
  .photo-fill { position: absolute; inset: 0 0 16px 0; }
  .photo-fill--wires { background: linear-gradient(180deg, #f1f1f1, #c8c8c8); }
  .photo-fill--hub { background: linear-gradient(180deg, #fafafa, #d9d4cf); }
  .photo-fill--tv { background: linear-gradient(180deg, #dfe3e8, #9aa1aa); }
  .photo-caption {
    position: absolute; left: 0; right: 0; bottom: 0; height: 16px;
    background: var(--ink); color: var(--white);
    font-size: 7px; font-weight: 600; letter-spacing: .05em;
    text-align: center; line-height: 16px; text-transform: uppercase;
  }
  .card--automation .phone-line {
    bottom: 34px; left: 28px;
    display: flex; align-items: center; gap: 8px;
    font-size: 20px; font-weight: 600; color: var(--white);
  }
</style>
</head>
<body>

<section class="card card--repairs" aria-label="Electronic repairs side">
  <svg class="card-shape" viewBox="0 0 380 660" aria-hidden="true">
    <rect width="380" height="260" fill="var(--pink)"/>
    <polygon points="0,0 160,0 0,200" fill="var(--pink-light)" opacity=".35"/>
    <polygon points="220,0 380,0 380,150" fill="var(--pink-deep)" opacity=".35"/>
    <rect x="40" y="124" width="72" height="22" fill="none" stroke="rgba(255,255,255,.25)"/>
    <rect x="160" y="118" width="60" height="28" fill="none" stroke="rgba(255,255,255,.25)"/>
    <rect x="270" y="116" width="70" height="30" fill="none" stroke="rgba(255,255,255,.25)"/>
    <polygon points="0,230 190,300 380,230 380,260 190,320 0,260" fill="var(--grey)"/>
    <polygon points="0,300 90,280 60,440 0,440" fill="var(--grey)"/>
    <polygon points="380,300 290,280 320,440 380,440" fill="var(--grey-mid)" opacity=".6"/>
  </svg>
  <div class="wordmark">QUILLAN</div>
  <div class="device-labels">
    <span class="device-label">LAPTOPS</span>
    <span class="device-label">MOBILES</span>
    <span class="device-label">TABLETS</span>
  </div>
  <div class="device-illustration" role="img" aria-label="Group of devices with cracked screens: monitor, tablet, phone, laptop and watch"></div>
  <p class="tagline">For any repairs, we come to you,<br>with unbeatable prices</p>
  <p class="service-title">ALL ELECTRONIC REPAIRS</p>
  <div class="phone-pill">
    <svg width="16" height="20" viewBox="0 0 16 20" aria-hidden="true"><rect x="3" y="1" width="10" height="18" rx="2" fill="none" stroke="var(--pink)" stroke-width="2"/><circle cx="8" cy="15.5" r="1.2" fill="var(--pink)"/></svg>
    (555) 314-2790
  </div>
  <div class="email-line">
    <svg width="16" height="12" viewBox="0 0 16 12" aria-hidden="true"><rect x="1" y="1" width="14" height="10" fill="none" stroke="var(--ink)" stroke-width="1.5"/><path d="M1 1 L8 7 L15 1" fill="none" stroke="var(--ink)" stroke-width="1.5"/></svg>
    Help@Quillan-example.support
  </div>
</section>

<section class="card card--automation" aria-label="Home automation side">
  <svg class="card-shape" viewBox="0 0 380 660" aria-hidden="true">
    <defs>
      <linearGradient id="darkFade" x1="0" y1="0" x2="1" y2="1">
        <stop offset="0" stop-color="#2e2e33"/>
        <stop offset="1" stop-color="#18181b"/>
      </linearGradient>
    </defs>
    <rect width="380" height="660" fill="url(#darkFade)"/>
    <polygon points="0,468 190,548 380,440 380,470 190,578 0,498" fill="var(--white)"/>
    <polygon points="0,508 190,588 380,480 380,660 0,660" fill="var(--pink)"/>
    <polygon points="220,560 380,470 380,420" fill="var(--pink)"/>
  </svg>
  <div class="wordmark">QUILLAN</div>
  <h2 class="side-title">HOME AUTOMATION</h2>
  <ul class="service-list">
    <li class="service-item"><svg width="14" height="14" viewBox="0 0 14 14" aria-hidden="true"><circle cx="7" cy="7" r="7" fill="var(--pink)"/><path d="M5.5 4 L8.5 7 L5.5 10" fill="none" stroke="var(--ink)" stroke-width="1.6"/></svg>Security Camera Installation</li>
    <li class="service-item"><svg width="14" height="14" viewBox="0 0 14 14" aria-hidden="true"><circle cx="7" cy="7" r="7" fill="var(--pink)"/><path d="M5.5 4 L8.5 7 L5.5 10" fill="none" stroke="var(--ink)" stroke-width="1.6"/></svg>Sink Installation</li>
    <li class="service-item"><svg width="14" height="14" viewBox="0 0 14 14" aria-hidden="true"><circle cx="7" cy="7" r="7" fill="var(--pink)"/><path d="M5.5 4 L8.5 7 L5.5 10" fill="none" stroke="var(--ink)" stroke-width="1.6"/></svg>Fireplace Mounting</li>
    <li class="service-item"><svg width="14" height="14" viewBox="0 0 14 14" aria-hidden="true"><circle cx="7" cy="7" r="7" fill="var(--pink)"/><path d="M5.5 4 L8.5 7 L5.5 10" fill="none" stroke="var(--ink)" stroke-width="1.6"/></svg>Chandelier Installation</li>
    <li class="service-item"><svg width="14" height="14" viewBox="0 0 14 14" aria-hidden="true"><circle cx="7" cy="7" r="7" fill="var(--pink)"/><path d="M5.5 4 L8.5 7 L5.5 10" fill="none" stroke="var(--ink)" stroke-width="1.6"/></svg>Television &amp; Sound Bar Mounting<br>(Hidden Wires Optional)</li>
  </ul>
  <div class="photo-row">
    <div class="photo-tile">
      <div class="photo-fill photo-fill--wires" role="img" aria-label="Wall-mounted TV with hidden wiring"></div>
      <span class="photo-caption">Hidden Wires</span>
    </div>
    <div class="photo-tile">
      <div class="photo-fill photo-fill--hub" role="img" aria-label="Smart home devices and thermostat"></div>
      <span class="photo-caption">Home Automation</span>
    </div>
    <div class="photo-tile">
      <div class="photo-fill photo-fill--tv" role="img" aria-label="Mounted television with sound bar"></div>
      <span class="photo-caption">Soundbar &amp; TV Mounting</span>
    </div>
  </div>
  <div class="phone-line">
    <svg width="16" height="20" viewBox="0 0 16 20" aria-hidden="true"><rect x="3" y="1" width="10" height="18" rx="2" fill="none" stroke="var(--white)" stroke-width="2"/><circle cx="8" cy="15.5" r="1.2" fill="var(--white)"/></svg>
    (555) 314-2790
  </div>
</section>

</body>
</html>
```